Judicial election website to attract voters

I need a simple one-page web design for a judicial election. I'm going to put up one picture, maybe two. The picture I have needs a little touch-up (whiten teeth for example). I have 3 paragraphs of text. I'd like a "Donate" button that can link to a Tillwisp account. I'd also like a little background design, like the Constitution or something like that. There's a couple other little things but that's the bulk of it.

Target Market(s)

Involved voters and some media

Industry/Entity Type

Legal

Number of Pages Required

1 page

Font styles to use
Sans Serif

Requirements
Must have
• My picture, text, donate button
• Phrase "Remember to vote August 30, 2016!"
Nice to have
• Perhaps a second photo, maybe a short 30 second video of me talking directly to the voters, cool background: Constitution, something judgey.
Should not have
• Not sure ... profanity, I guess.

```html
<!DOCTYPE html>
<html lang="en">
<head>
<meta charset="utf-8">
<title>Menu — Judicial Election</title>
<link rel="stylesheet" href="https://fonts.googleapis.com/css2?family=Lato:wght@700&family=Zilla+Slab:wght@700&display=swap">
<style>
  :root {
    --bg: #1f222a;
    --accent: #f14b4f;
    --button-face: #ffffff;
  }
  * { margin: 0; padding: 0; box-sizing: border-box; }
  html, body {
    width: 1200px;
    height: 545px;
    overflow: hidden;
    background: var(--bg);
  }
  .menu-overlay {
    position: relative;
    width: 1200px;
    height: 545px;
    background: var(--bg);
  }
  .donate-link {
    position: absolute;
    top: 52px;
    right: 160px;
    display: flex;
    align-items: center;
    gap: 6px;
    color: var(--accent);
    text-decoration: none;
    font-family: "Zilla Slab", Georgia, serif;
    font-weight: 700;
    font-size: 25px;
    line-height: 28px;
  }
  .close-button {
    position: absolute;
    top: 49px;
    left: 1076px;
    width: 35px;
    height: 35px;
    border: 0;
    background: none;
    cursor: pointer;
  }
  .close-button svg { display: block; width: 35px; height: 35px; }
  .main-nav {
    position: absolute;
    left: 0;
    right: 0;
    top: 0;
    font-family: "Lato", Arial, sans-serif;
    font-weight: 700;
    font-size: 48px;
    line-height: 48px;
  }
  .main-nav a {
    position: absolute;
    left: 50%;
    transform: translateX(-50%);
    white-space: nowrap;
    color: var(--accent);
    text-decoration: none;
  }
  .nav-save { top: 171px; }
  .nav-about { top: 245px; }
  .nav-contact { top: 329px; }
  .nav-about.is-active::after {
    content: "";
    position: absolute;
    left: 0;
    right: 0;
    top: 51px;
    height: 6px;
    background: var(--accent);
  }
</style>
</head>
<body>
  <div class="menu-overlay">
    <a class="donate-link" href="#donate">
      <span class="donate-provider">Tillwisp</span>
      <span class="donate-label">donate</span>
    </a>
    <button class="close-button" aria-label="Close menu">
      <svg viewBox="0 0 35 35" aria-hidden="true">
        <circle cx="17.5" cy="17.5" r="17.5" fill="var(--button-face)"/>
        <path d="M11.5 11.5 L23.5 23.5 M23.5 11.5 L11.5 23.5" stroke="var(--accent)" stroke-width="4.5" stroke-linecap="round"/>
      </svg>
    </button>
    <nav class="main-nav">
      <a class="nav-save" href="#save-the-date">SAVE THE DATE</a>
      <a class="nav-about is-active" href="#about">ABOUT</a>
      <a class="nav-contact" href="#contact">CONTACT</a>
    </nav>
  </div>
</body>
</html>
```